Plakat für Hersteller von maßgefertigten Tischunikaten aus Massivholz
Zielgruppe
Wir sind einen Firma die sich auf die Fertigung von maßgefertigten Tischunikaten aus Massivholz spezialisiert hat. Unsere Zielgruppe sind Design affine Leute, im Alter von 35-55 Jahren
Aufgabenstellung
Wir benötigen das Design für eine Messewand mit den Maßen 443X227 cm. 5 Zentimeter rundlaufen dürfen keine Elemente mehr platziert werden. Die Messewand steht im Hintergrund von unserem Stand bei verschiedenen Designmessen
Infos die auf die Messewand müssen: Logo, Tischmanufaktur aus Stuttgart, Maßgefertigte Tischunikate (Bei der Formulierung bin ich flexibel, ihr könnt bspw. auch nur Stichworte benutzen, aber Stuttgart und maßgefertigt ist wichtig).
Die Messewand soll sehr minimalistisch gestaltet sein, bei der letzten Messewand hatten wir ein Foto von einem Tisch im Hintergrund und das sah merkwürdig aus.

```html
<!DOCTYPE html>
<html lang="de">
<head>
<meta charset="utf-8">
<title>Holtzberg Manufaktur – Messewand</title>
<link rel="stylesheet" href="https://fonts.googleapis.com/css2?family=Anton&family=Montserrat:wght@300;700&display=swap">
<style>
  :root {
    --page: #ece9e3;
    --slate-dark: #0d0d0d;
    --slate-mid: #1f1f1f;
    --ink-light: #dcdcdc;
    --wood-light: #c98a4b;
    --wood-dark: #8f4f1f;
  }
  * { margin: 0; padding: 0; box-sizing: border-box; }
  html, body {
    width: 1200px;
    height: 1117px;
    overflow: hidden;
    background: var(--page);
  }
  .trade-wall {
    position: absolute;
    left: 0;
    top: 251px;
    width: 1200px;
    height: 615px;
    overflow: hidden;
    background:
      radial-gradient(ellipse at 45% 20%, var(--slate-mid) 0%, var(--slate-dark) 70%);
    color: var(--ink-light);
  }
  .wall-shapes {
    position: absolute;
    inset: 0;
    width: 1200px;
    height: 615px;
  }
  .brand-mark {
    position: absolute;
    left: 85px;
    top: 98px;
    width: 352px;
    height: 352px;
    border: 24px solid var(--ink-light);
    border-radius: 50%;
  }
  .brand-name {
    position: absolute;
    left: 60px;
    top: 470px;
    width: 402px;
    text-align: center;
    font-family: "Montserrat", sans-serif;
    font-weight: 300;
    font-size: 24px;
    letter-spacing: 6px;
    text-transform: uppercase;
  }
  .headline {
    position: absolute;
    left: 487px;
    top: 118px;
    font-family: "Anton", sans-serif;
    font-weight: 400;
    text-transform: uppercase;
    line-height: 1;
    letter-spacing: -0.5px;
  }
  .headline-line1 { display: block; font-size: 74px; }
  .headline-line2 { display: block; font-size: 94px; margin-top: 6px; }
  .tagline {
    position: absolute;
    left: 489px;
    top: 354px;
    width: 417px;
    height: 69px;
    border-top: 2px solid var(--ink-light);
    border-bottom: 2px solid var(--ink-light);
    display: flex;
    align-items: center;
    font-family: "Montserrat", sans-serif;
    font-weight: 700;
    font-size: 28px;
    letter-spacing: 9px;
  }
  .social-handle {
    position: absolute;
    left: 491px;
    top: 494px;
    display: flex;
    align-items: center;
    gap: 10px;
    font-family: "Montserrat", sans-serif;
    font-weight: 300;
    font-size: 19px;
    letter-spacing: 3px;
    text-transform: uppercase;
  }
  .social-dot {
    width: 24px;
    height: 24px;
    border: 2px solid var(--ink-light);
    border-radius: 6px;
  }
</style>
</head>
<body>
  <section class="trade-wall">
    <svg class="wall-shapes" viewBox="0 0 1200 615" xmlns="http://www.w3.org/2000/svg">
      <defs>
        <linearGradient id="woodTone" x1="0" y1="0" x2="1" y2="0">
          <stop offset="0" stop-color="var(--wood-light)"/>
          <stop offset="0.5" stop-color="var(--wood-dark)"/>
          <stop offset="1" stop-color="var(--wood-light)"/>
        </linearGradient>
      </defs>
      <path class="divider-band" fill="var(--ink-light)"
        d="M1126,0 C1160,120 1110,195 1040,262 L965,330 C925,365 906,385 906,425 L906,615 L1200,615 L1200,0 Z"/>
      <path class="wood-panel" fill="url(#woodTone)" role="img" aria-label="Massivholz-Oberfläche mit Maserung"
        d="M1172,0 C1205,125 1150,220 1075,290 L995,360 C950,395 938,410 938,450 L938,615 L1200,615 L1200,0 Z"/>
    </svg>

    <div class="brand-mark"></div>
    <p class="brand-name">Holtzberg Manufaktur</p>

    <h1 class="headline">
      <span class="headline-line1">Tischmanufaktur</span>
      <span class="headline-line2">aus Stuttgart</span>
    </h1>

    <p class="tagline">MAẞGEFERTIGT</p>

    <p class="social-handle"><span class="social-dot"></span>holtzberg_manufaktur</p>
  </section>
</body>
</html>
```